Real Estate 24"x24" Sign, Business Card, Letter Head and Envelope

This is a 4 project contest. If we choose a design or designs we like from what you sent we are willing to pay an amount at our discretion for that design even if we don't like all your designs for the 4 projects. Please be creative. Attached are our logo files. Please message us with any questions. Thanks and Good Luck!
Project 1: QMTD Realty 24" x 24" yard sign
We want to use the same blue background in our logo for the sign where the logo in white font will be on. CMYK 100,80,0,0. Attached is a sample a local designer made for you to get an idea what we are looking for. In the sample, the website is way too big and the entire sign is very plain and not attractive looking plus blue color is wrong one. We want the logo on top as large as possible but keeping it proportionate and attractive looking buy not too big that it looks odd. The following information can go in white color background or same blue color background color. Our company colors are blue (as per logo), green (as per logo), and white. "Residential & Commercial" goes under the logo. Under that put our phone number "312-640-5918" as large as possible but still looks good and under that our website in much smaller but readable font "www.qmtdrealty.com".
Project 2: Envelope
We have two version of the logo. Use one or both. Whatever looks best in your design. The envelope will be white. We only want on top left corner logo and underneath our mailing address: 5147 Hawthorne Ave. Skokie, IL 60091-2714. Maybe some creative decorative design at bottom of envelope will look nice
Project 3: Letter Head
We have two version of the logo. Use one or both. Whatever looks best in your design. We want the following information on the top of the letterhead. Logo, address: 5147 Hawthorne Ave., Skokie, IL 60091-2714, phone: 312-640-5918, fax: 312-918-6057 website www.qmtdrealty.com, email: info@qmtdrealty.com
Project 4: Business card
Use either logo. We need cards for two individuals. Information for Person 1: Dev Mehta, Managing Broker, Phone: 312-640-5918, Email: dev.mehta@qmtdrealty.com. Person 2: Raj Mehta Broker Phone: 312-285-3390 Email: raj.mehta@qmtdrealty.com. Add Address, Fax and website same as above letter head.

```html
<!DOCTYPE html>
<html lang="en">
<head>
<meta charset="utf-8">
<title>QMTD Realty Yard Sign</title>
<link rel="stylesheet" href="https://fonts.googleapis.com/css2?family=Montserrat:ital,wght@0,500;0,700;1,600&display=swap">
<style>
  :root {
    --brand-blue: #034ea2;
    --brand-green: #7dc242;
    --sign-white: #ffffff;
    --backdrop: #e4e4e4;
  }
  * { margin: 0; padding: 0; box-sizing: border-box; }
  html, body {
    width: 1200px;
    height: 1000px;
    overflow: hidden;
    background: var(--backdrop);
    font-family: "Montserrat", sans-serif;
  }
  .yard-sign {
    position: absolute;
    left: 196px;
    top: 75px;
    width: 809px;
    height: 808px;
    background: var(--sign-white);
    overflow: hidden;
  }
  .sign-header-art {
    position: absolute;
    inset: 0;
    width: 809px;
    height: 808px;
  }
  .brand-name {
    position: absolute;
    left: 0;
    right: 0;
    top: 150px;
    text-align: center;
    color: var(--sign-white);
    font-weight: 700;
    font-size: 128px;
    line-height: 1.05;
    letter-spacing: 4px;
  }
  .sign-details {
    position: absolute;
    left: 0;
    right: 0;
    text-align: center;
    color: var(--brand-blue);
  }
  .service-line {
    top: 575px;
    font-weight: 500;
    font-size: 40px;
  }
  .phone-number {
    top: 632px;
    font-weight: 700;
    font-size: 82px;
    letter-spacing: 1px;
  }
  .website {
    top: 728px;
    font-weight: 600;
    font-style: italic;
    font-size: 44px;
  }
</style>
</head>
<body>
  <main class="yard-sign">
    <svg class="sign-header-art" viewBox="0 0 809 808" aria-hidden="true">
      <path class="accent-swoosh" d="M0 482 Q404.5 612 809 482 V512 Q404.5 612 0 512 Z" fill="var(--brand-green)"/>
      <path class="header-panel" d="M0 0 H809 V485 Q404.5 618 0 485 Z" fill="var(--brand-blue)"/>
    </svg>
    <h1 class="brand-name">QMTD<br>Realty</h1>
    <p class="sign-details service-line">Residential &amp; Commercial</p>
    <p class="sign-details phone-number">312-640-5918</p>
    <p class="sign-details website">qmtdrealty.com</p>
  </main>
</body>
</html>
```